Modern Employee Handbook Cover Design Needed

I need help. I am designing a 50+ page Employee Handbook and want a great cover design. I'm looking for a great cover because our company has changed so much in the past years since the last handbook was published and I want to signify and celebrate all the positive things we have done. It may not seem like such a big deal but I'm trying to make a big impact.

I'm looking for something interesting. Employee Handbooks are the most boring things int he world but I don't ours to LOOK that way. I want creative, modern, slick, clean, whatever you want that would make someone want to look at (even if it is for a second). It does NOT need to even be called an Employee Handbook (I'm really open to ideas)

This will be a typical 8.5 x 11 book format. 70% of our employees are under the age of 40 and are in CA, MA, FL, and IN.

The final design should communicate that we are not the same company we were a few years ago but instead we are more modern and current.

Target Market(s)

Most of our employees are under 40 years old. They are well educated. We are a national company with employees in CA, MA, FL and IN

Industry/Entity Type

Education

Font styles to use
Serif
Sans Serif
Other font styles liked:
• I like the fonts used by velmo but am open to ANY fonts.

Requirements
Must have
• Modern, up to date designs, unexpected, unique, cool, etc...
Should not have
• I don't like the typical teamwork images, world and globe things, or tree supporting branch type things that Human Resources and Employee Handbooks often is represented by in print. They are so boring to me. https://www.trelvasearch.com/search?q=human+resources+handbook&source=lnms&tbm=isch&sa=X&ved=0ahUKEwjl1oWHt67RAhULw1QKHWTaB0oQ_AUICCgB&biw=1920&bih=950
• No stick figures standing in a row or shaking hands. Stuff like that is so old.
• Our clients are young adults with Autism but I don't want puzzle pieces which is a universal symbol of Autism.

```html
<!DOCTYPE html>
<html lang="en">
<head>
<meta charset="utf-8">
<title>ZAL Employee Handbook Cover</title>
<link rel="stylesheet" href="https://fonts.googleapis.com/css2?family=Architects+Daughter&family=Roboto+Condensed:wght@700&display=swap">
<style>
  :root {
    --tan: #d8c184;
    --brown: #7b512c;
    --yellow: #f4c12b;
    --white: #ffffff;
    --tape: rgba(196, 222, 232, 0.62);
    --ink: #2a2a2a;
  }
  html, body {
    margin: 0;
    padding: 0;
    width: 927px;
    height: 1200px;
    overflow: hidden;
    background: var(--tan);
  }
  .cover {
    position: relative;
    width: 927px;
    height: 1200px;
    overflow: hidden;
  }
  .cover__bands,
  .cover__grain {
    position: absolute;
    inset: 0;
    width: 927px;
    height: 1200px;
  }
  .cover__grain {
    mix-blend-mode: multiply;
    opacity: 0.55;
    pointer-events: none;
    z-index: 5;
  }
  .cover__tape {
    position: absolute;
    left: 430px;
    top: 18px;
    width: 500px;
    height: 82px;
    background: var(--tape);
    transform: rotate(12deg);
    transform-origin: left top;
  }
  .cover__label {
    position: absolute;
    left: 455px;
    top: 24px;
    margin: 0;
    font-family: "Architects Daughter", cursive;
    font-size: 50px;
    font-weight: 400;
    color: var(--ink);
    letter-spacing: 1px;
    transform: rotate(13deg);
    transform-origin: left top;
    white-space: nowrap;
  }
  .cover__brand {
    position: absolute;
    left: 185px;
    top: 505px;
    margin: 0;
    font-family: "Roboto Condensed", sans-serif;
    font-weight: 700;
    font-size: 260px;
    line-height: 1;
    color: var(--yellow);
    transform: rotate(-20deg);
    transform-origin: left top;
  }
  .cover__tagline {
    position: absolute;
    left: 340px;
    top: 845px;
    margin: 0;
    font-family: "Roboto Condensed", sans-serif;
    font-weight: 700;
    font-size: 44px;
    line-height: 1.12;
    color: var(--white);
    transform: rotate(-20deg);
    transform-origin: left top;
    white-space: nowrap;
  }
</style>
</head>
<body>
<main class="cover">
  <svg class="cover__bands" viewBox="0 0 927 1200" aria-hidden="true">
    <defs>
      <linearGradient id="green-band" x1="0" y1="1" x2="1" y2="0">
        <stop offset="0" stop-color="#a3bb38"/>
        <stop offset="1" stop-color="#c8d162"/>
      </linearGradient>
      <linearGradient id="orange-band" x1="0" y1="1" x2="1" y2="0">
        <stop offset="0" stop-color="#c53c1b"/>
        <stop offset="1" stop-color="#dc5a20"/>
      </linearGradient>
    </defs>
    <rect class="band band--tan" width="927" height="1200" fill="var(--tan)"/>
    <path class="band band--green" d="M0 74 Q150 20 332 0 L927 0 L927 200 Q400 330 0 540 Z" fill="url(#green-band)"/>
    <path class="band band--brown" d="M0 540 Q400 330 927 200 L927 550 Q450 560 0 810 Z" fill="var(--brown)"/>
    <path class="band band--orange" d="M0 810 Q450 560 927 550 L927 1030 Q700 1100 480 1200 L0 1200 Z" fill="url(#orange-band)"/>
  </svg>

  <div class="cover__tape"></div>
  <p class="cover__label">Empolee HandBook</p>

  <h1 class="cover__brand">ZAL</h1>
  <p class="cover__tagline">Preparing Young Adults<br>with Learning Differences<br>for Success Since 1984</p>

  <svg class="cover__grain" viewBox="0 0 927 1200" aria-hidden="true">
    <filter id="grain-filter" x="0" y="0" width="100%" height="100%">
      <feTurbulence type="fractalNoise" baseFrequency="0.85" numOctaves="3" seed="7" result="noise"/>
      <feColorMatrix in="noise" type="matrix" values="0 0 0 0 0.25  0 0 0 0 0.18  0 0 0 0 0.1  0 0 0 1.6 -0.55"/>
    </filter>
    <rect width="927" height="1200" filter="url(#grain-filter)"/>
  </svg>
</main>
</body>
</html>
```